Design a business card for a hair barber [FAST TURNAROUND] [OTHER PROJECTS AVAILABLE]

I need to have this business card re-designed for a barbershop.

I want a new and eye-catching design and modern.

Please post your design in a mock-up for better presentation.

```html
<!DOCTYPE html>
<html lang="en">
<head>
<meta charset="utf-8">
<title>Keel Fine Cuts – Business Card</title>
<link rel="stylesheet" href="https://fonts.googleapis.com/css2?family=Ubuntu:ital,wght@0,400;0,500;0,700;1,400;1,700&family=Oswald:wght@300;400&display=swap">
<style>
  :root {
    --bg: #2b2e33;
    --paper: #ffffff;
    --blue: #2d6ec4;
    --slate: #3e5d80;
    --navy: #284a72;
    --red: #9a2a2e;
    --red-dark: #7d1f23;
    --ink: #1f2a36;
    --white: #ffffff;
  }
  * { box-sizing: border-box; margin: 0; padding: 0; }
  html, body { width: 1200px; height: 900px; overflow: hidden; }
  body {
    background: var(--bg);
    font-family: "Ubuntu", sans-serif;
    position: relative;
  }
  .card {
    position: absolute;
    left: 290px;
    width: 620px;
    height: 354px;
    overflow: hidden;
    background: var(--paper);
    box-shadow: 0 10px 28px rgba(0,0,0,.45);
  }
  .card--front { top: 66px; }
  .card--back { top: 480px; }
  .card__art { position: absolute; inset: 0; }

  .brand {
    position: absolute;
    display: flex;
    align-items: center;
    gap: 8px;
    color: var(--navy);
    font-weight: 700;
    font-size: 22px;
  }
  .brand__dot {
    width: 14px; height: 14px;
    border-radius: 50%;
    background: var(--navy);
  }
  .card--front .brand { left: 40px; top: 34px; }
  .card--back .brand { right: 40px; top: 96px; }

  .discount {
    position: absolute;
    left: 48px; top: 92px;
    font-weight: 700; font-style: italic;
    font-size: 17px; line-height: 1.1;
    color: var(--navy);
    text-align: center;
  }
  .discount__amount { color: var(--red); }

  .shop-name {
    position: absolute;
    right: 26px; top: 158px;
    width: 230px;
    text-align: center;
    color: var(--white);
    font-family: "Oswald", sans-serif;
    font-weight: 300;
    letter-spacing: 2px;
    font-size: 17px;
    line-height: 1.15;
  }
  .shop-name__sub { display: block; font-size: 14px; letter-spacing: 1px; }

  .contact {
    position: absolute;
    left: 330px; top: 222px;
    color: var(--white);
    font-size: 16px;
    line-height: 1.2;
  }
  .contact__hours { font-size: 20px; font-weight: 500; }
  .contact__hours small { display: block; font-size: 15px; font-weight: 400; margin-bottom: 4px; }
  .contact__row { display: flex; align-items: center; gap: 7px; }
  .contact__icon {
    width: 15px; height: 15px; border-radius: 50%;
    background: var(--red);
    display: inline-flex; align-items: center; justify-content: center;
  }

  .email {
    position: absolute;
    left: 40px; bottom: 11px;
    display: flex; align-items: center; gap: 10px;
    color: var(--white);
    font-size: 16px;
    letter-spacing: .5px;
  }

  .about {
    position: absolute;
    left: 26px; top: 34px;
    width: 290px;
    color: var(--white);
    font-style: italic;
    font-size: 12.5px;
    line-height: 1.45;
  }
  .tagline {
    position: absolute;
    right: 34px; top: 236px;
    color: var(--blue);
    font-style: italic;
    font-weight: 500;
    font-size: 15px;
  }
  .social {
    position: absolute;
    left: 250px; bottom: 26px;
    display: flex; gap: 10px;
  }
  .social__badge {
    width: 30px; height: 30px;
    border-radius: 6px;
    background: var(--slate);
    border: 2px solid var(--white);
    box-shadow: 0 2px 4px rgba(0,0,0,.3);
  }
  .social__badge--blue { background: var(--blue); }
  .social__badge--green { background: #3d8a45; }
  .social__badge--grey { background: #6b7280; }
</style>
</head>
<body>

<section class="card card--front" aria-label="Card front">
  <svg class="card__art" viewBox="0 0 620 354" aria-hidden="true">
    <rect width="620" height="354" fill="var(--slate)"/>
    <polygon points="0,0 620,0 620,140 300,158 0,158" fill="var(--paper)"/>
    <polygon points="380,150 620,136 620,206 380,206" fill="var(--blue)"/>
    <polygon points="190,190 420,120 424,138 196,212" fill="var(--red)"/>
    <polygon points="250,176 450,112 452,126 254,190" fill="var(--blue)"/>
    <polygon points="300,170 470,118 472,130 302,182" fill="var(--red-dark)"/>
    <line x1="330" y1="214" x2="600" y2="214" stroke="var(--red)" stroke-width="1"/>
    <rect x="0" y="312" width="620" height="42" fill="var(--blue)"/>
  </svg>

  <div class="brand"><span class="brand__dot"></span>Keel Fine Cuts</div>
  <p class="discount"><span class="discount__amount">30% OFF</span><br>DISCOUNT</p>
  <p class="shop-name">KEEL FINE CUTS<span class="shop-name__sub">(Hair Services)</span></p>

  <div class="contact">
    <p class="contact__hours">Mon-Sat<small>(9am-7pm)</small></p>
    <p class="contact__row">
      <span class="contact__icon"><svg width="9" height="9" viewBox="0 0 10 10"><path d="M2 1 L4 1 L4.6 3 L3.4 3.8 Q4.4 5.8 6.2 6.6 L7 5.4 L9 6 L9 8 Q5 9 2 5 Q1 3 2 1Z" fill="#fff"/></svg></span>
      510-555-0142
    </p>
    <p class="contact__row">
      <span class="contact__icon"><svg width="9" height="9" viewBox="0 0 10 10"><path d="M5 0.5 A3.2 3.2 0 0 1 8.2 3.7 C8.2 6 5 9.5 5 9.5 C5 9.5 1.8 6 1.8 3.7 A3.2 3.2 0 0 1 5 0.5Z M5 2.5 A1.2 1.2 0 1 0 5 4.9 A1.2 1.2 0 1 0 5 2.5Z" fill="#fff"/></svg></span>
      2215 Alder Ave.
    </p>
  </div>

  <p class="email">
    <span class="contact__icon"><svg width="9" height="9" viewBox="0 0 10 10"><rect x="1" y="2" width="8" height="6" fill="none" stroke="#fff"/><path d="M1 2 L5 5.5 L9 2" fill="none" stroke="#fff"/></svg></span>
    finecuts22@mailbox.com
  </p>
</section>

<section class="card card--back" aria-label="Card back">
  <svg class="card__art" viewBox="0 0 620 354" aria-hidden="true">
    <rect width="620" height="354" fill="var(--paper)"/>
    <polygon points="0,0 330,0 330,220 300,240 250,354 0,354" fill="var(--blue)"/>
    <polygon points="336,0 356,0 342,210 322,214" fill="var(--red)"/>
    <polygon points="360,0 374,0 372,200 356,204" fill="var(--slate)"/>
    <polygon points="250,354 300,240 330,220 620,220 620,354" fill="var(--red)"/>
    <polygon points="282,354 322,260 620,260 620,354" fill="var(--red-dark)" opacity=".35"/>
    <polygon points="300,240 330,220 620,220 620,262 310,262" fill="var(--paper)"/>
  </svg>

  <p class="about">“Keel Fine Cuts is a family-orientated hair styling shop. We listen to our clients needs, wants and fulfill them within the business guidelines. We provide a pleasant environment for all ages and ethnicities.”</p>
  <div class="brand"><span class="brand__dot"></span>Keel Fine Cuts</div>
  <p class="tagline">“Providing the style for the bay”</p>
  <div class="social" aria-label="Social channels">
    <span class="social__badge social__badge--blue"></span>
    <span class="social__badge"></span>
    <span class="social__badge social__badge--green"></span>
    <span class="social__badge social__badge--grey"></span>
    <span class="social__badge social__badge--blue"></span>
  </div>
</section>

</body>
</html>
```